Weekly Newsletter template for our niche within the Telecom Industry

We need a 'skeleton' format where we can insert our weekly information and ads.
We will do all the content in-house.
Content in both info and ads must be able to contain hyperlinks.
Our company website is: www. halverd-quenby.com
We think we would like something similar to the top format but with the single bar on the right side as a place to insert ads
Thank you.

```html
<!DOCTYPE html>
<html lang="en">
<head>
<meta charset="utf-8">
<title>Halverd Quenby — Weekly Newsletter</title>
<link rel="stylesheet" href="https://fonts.googleapis.com/css2?family=Poppins:wght@300;400;500;600;700&display=swap">
<style>
  :root {
    --backdrop: #d3d3d3;
    --paper: #ffffff;
    --ink-dark: #2d2f30;
    --ink-body: #333536;
    --accent: #20b6d2;
    --accent-lime: #c2d23f;
    --on-dark: #ffffff;
  }
  * { margin: 0; padding: 0; box-sizing: border-box; }
  html, body { width: 1038px; height: 1200px; overflow: hidden; }
  body {
    background: var(--backdrop);
    font-family: "Poppins", sans-serif;
    color: var(--ink-body);
    position: relative;
  }
  a { color: inherit; text-decoration: none; }

  .newsletter {
    position: absolute; left: 193px; top: 139px;
    width: 651px; height: 921px;
    background: var(--paper);
    box-shadow: 0 6px 24px rgba(0,0,0,0.18);
    overflow: hidden;
  }
  .masthead {
    position: absolute; left: 0; top: 0; width: 651px; height: 276px;
    background: var(--ink-dark);
  }
  .volume-tag {
    position: absolute; left: 44px; top: 43px; width: 117px; height: 27px;
    background: var(--accent); color: var(--on-dark);
    font-size: 20px; font-weight: 400; line-height: 27px; padding-left: 8px;
  }
  .masthead-title {
    position: absolute; left: 43px; top: 82px;
    color: var(--on-dark); font-size: 45px; font-weight: 600;
    line-height: 45px; letter-spacing: 0.2px;
  }
  .masthead-subtitle {
    position: absolute; left: 44px; top: 216px;
    color: var(--accent); font-size: 22px; font-weight: 400; line-height: 28px;
  }

  /* Right column */
  .brand-box {
    position: absolute; left: 377px; top: 0; width: 240px; height: 102px;
    background: var(--paper);
    display: flex; align-items: center; justify-content: center; gap: 10px;
  }
  .brand-dot { width: 14px; height: 14px; border-radius: 50%; background: var(--accent); }
  .brand-name { font-size: 18px; font-weight: 600; color: var(--ink-dark); letter-spacing: 0.5px; }

  .feature-box {
    position: absolute; left: 377px; top: 102px; width: 240px; height: 363px;
    background: var(--accent); color: var(--on-dark);
  }
  .feature-title {
    position: absolute; left: 22px; top: 23px;
    font-size: 21px; font-weight: 600; line-height: 28px;
  }
  .feature-body {
    position: absolute; left: 22px; top: 61px; width: 214px;
    font-size: 11.2px; line-height: 17.5px; font-weight: 400;
  }
  .read-more {
    position: absolute; right: 0; width: 83px; height: 18px;
    background: var(--ink-dark); color: var(--on-dark);
    font-size: 8.6px; line-height: 19px; text-align: center;
  }
  .feature-box .read-more { bottom: 0; }

  .ad-slot { position: absolute; left: 377px; width: 240px; height: 199px; }
  .ad-slot .read-more { bottom: 0; }
  .ad-ai {
    top: 469px;
    background: radial-gradient(circle at 58% 36%, #7fe0ff 0%, #1f8fd6 18%, #0e5f9e 55%, #0a3f6e 100%);
  }
  .ad-tower {
    top: 672px;
    background: linear-gradient(160deg, #b7cdee 0%, #8fb0e2 45%, #c9dbf2 100%);
  }

  .site-link {
    position: absolute; right: 34px; top: 891px;
    display: flex; align-items: center; gap: 4px;
    font-size: 8.4px; color: var(--ink-body);
  }
  .footer-bar {
    position: absolute; left: 0; bottom: 0; width: 651px; height: 8px;
    background: var(--ink-dark);
  }

  /* Main column (positions relative to the page) */
  .main-article { position: absolute; left: 45px; top: 0; width: 320px; height: 900px; }
  .accent-rule {
    position: absolute; left: 2px; top: 317px; width: 66px; height: 7px;
    background: linear-gradient(90deg, var(--accent) 30%, var(--accent-lime));
  }
  .article-heading {
    position: absolute; left: 0; top: 331px; width: 320px;
    font-size: 26.5px; font-weight: 600; line-height: 26px; color: var(--ink-dark);
  }
  .sub-heading {
    position: absolute; left: 0;
    font-size: 13.2px; font-weight: 700; color: var(--ink-dark); line-height: 16px;
  }
  .copy {
    position: absolute; left: 0; width: 320px;
    font-size: 11px; line-height: 13.2px; white-space: nowrap;
  }
  .copy.strong { font-weight: 600; color: var(--ink-dark); }
  .pull-quote {
    position: absolute; left: 0; top: 615px; width: 306px; height: 49px;
    border-top: 1.2px solid var(--accent); border-bottom: 1.2px solid var(--accent);
  }
  .pull-quote p {
    position: absolute; left: 0; top: 10px; white-space: nowrap;
    font-size: 11px; line-height: 13px; font-weight: 600; color: var(--accent);
  }
  .check-list { position: absolute; left: 0; top: 820px; list-style: none; }
  .check-list li {
    display: flex; align-items: center; gap: 10px;
    font-size: 11px; line-height: 17.5px; white-space: nowrap;
  }
</style>
</head>
<body>
  <article class="newsletter">
    <header class="masthead">
      <div class="volume-tag">Volume 01</div>
      <h1 class="masthead-title">YOUR<br>COMPANY<br>NEWS LETTER</h1>
      <p class="masthead-subtitle">WEEKLY UPDATE</p>
    </header>

    <div class="brand-box">
      <span class="brand-dot"></span>
      <span class="brand-name">HALVERD QUENBY</span>
    </div>

    <aside class="feature-box">
      <h2 class="feature-title">Hedding</h2>
      <p class="feature-body">explabora corehenda dolum si occatem accum nim rae velitibus et reped qui ommo optati simusa quam de dolessi bla verrore mpore, que nonse exerit autat estiunt andelestis voluptamus dunt excerios aut ommolest Citaerferrunt ad ut laturit emolore henestias doluptam ipid utemquae et fuga. Ut et a et evelit labo. Enisti ra cus eaque perem que preratqui ad ut eum faccabo. Tis est porum essinte necus.<br>Usa volut quam lautaquibus et, sectore vel inihil ipis exercit</p>
      <a class="read-more" href="#">Read More...</a>
    </aside>

    <div class="ad-slot ad-ai" role="img" aria-label="Photo of a hand touching a glowing AI circuit interface with connected document icons">
      <a class="read-more" href="#">Read More...</a>
    </div>
    <div class="ad-slot ad-tower" role="img" aria-label="Photo of a telecom transmission tower with signal waves against a soft blue sky">
      <a class="read-more" href="#">Read More...</a>
    </div>

    <section class="main-article">
      <span class="accent-rule"></span>
      <h2 class="article-heading">This is Heading This is Heading</h2>

      <h3 class="sub-heading" style="top:400px">THIS IS SUB HEADING</h3>
      <p class="copy" style="top:417px">Iliquiat urepedi volorrovitia voluptae perovita volupti<br>usdant verum dit dolest laciam eria sent ra doluptaspit<br>rerferum repudip icium, simporiorem rem evel<br>invendigene diae nusa sim quate nis ditatibus samus</p>
      <p class="copy strong" style="top:475px">excessus voluptae verum fugit ipsapit ute volo mo tore<br>sitatendit alicius doluptaqui doluptatio.</p>
      <p class="copy" style="top:507px">usdant verum dit dolest laciam eria sent ra doluptaspit<br>rerferum repudip icium, simporiorem rem evel</p>
      <p class="copy strong" style="top:539px">excessus voluptae verum fugit ipsapit ute volo mo tore<br>sitatendit alicius doluptaqui doluptatio.</p>
      <p class="copy" style="top:570px">usdant verum dit dolest laciam eria sent ra doluptaspit<br>rerferum repudip icium, simporiorem rem evel</p>

      <blockquote class="pull-quote">
        <p>usdant verum dit dolest laciam eria sent ra doluptaspit<br>rerferum repudip icium, simporiorem rem evel</p>
      </blockquote>

      <h3 class="sub-heading" style="top:679px">THIS IS SUB HEADING</h3>
      <p class="copy" style="top:697px;line-height:14.5px">Iliquiat urepedi volorrovitia voluptae perovita volupti<br>usdant verum dit dolest laciam eria sent ra doluptaspit<br>rerferum repudip icium, simporiorem rem evel</p>

      <h3 class="sub-heading" style="top:760px">THIS IS SUB HEADING</h3>
      <p class="copy" style="top:780px;line-height:15.6px">Et maximinis as della et aut et quia doluptae quis<br>molendi tiuntur,</p>

      <ul class="check-list">
        <li><svg width="10" height="10" viewBox="0 0 10 10" aria-hidden="true"><circle cx="5" cy="5" r="5" fill="#20b6d2"/><path d="M2.7 5.1 L4.3 6.6 L7.3 3.6" stroke="#fff" stroke-width="1.2" fill="none"/></svg>Verempo reptatet: magnis asi cus alitas</li>
        <li><svg width="10" height="10" viewBox="0 0 10 10" aria-hidden="true"><circle cx="5" cy="5" r="5" fill="#20b6d2"/><path d="M2.7 5.1 L4.3 6.6 L7.3 3.6" stroke="#fff" stroke-width="1.2" fill="none"/></svg>Verempo reptatet: magnis asi cus alitas</li>
      </ul>
    </section>

    <a class="site-link" href="#">
      <svg width="11" height="11" viewBox="0 0 12 12" aria-hidden="true" fill="none" stroke="#20b6d2" stroke-width="1">
        <circle cx="6" cy="6" r="5.2"/><ellipse cx="6" cy="6" rx="2.3" ry="5.2"/><line x1="0.8" y1="6" x2="11.2" y2="6"/>
      </svg>
      www. halverd-quenby.com
    </a>
    <div class="footer-bar"></div>
  </article>
</body>
</html>
```